Landing Page
Zielgruppe
Coaching. Zielgruppe Führungskräfte
Aufgabenstellung
Landingpage muss in Wordpress angebunden werden können. Corporate-Design siehe Webseite und Dateianhänge

```html
<!DOCTYPE html>
<html lang="de">
<head>
<meta charset="utf-8">
<title>Sabine Hollert – Pferdegestütztes Leadership-Coaching</title>
<link href="https://fonts.googleapis.com/css2?family=Playfair+Display:ital,wght@0,600;0,700;0,800;1,400&family=Inter:ital,wght@0,400;0,500;0,600;0,700;1,400;1,500&display=swap" rel="stylesheet">
<style>
:root{
  --bg:#0e0c13;
  --card:#1a1821;
  --card-line:#2a2732;
  --pink:#e8507d;
  --pink-soft:#f07a98;
  --pink-grad:linear-gradient(90deg,#f0527f,#d6457a);
  --text:#ffffff;
  --muted:#c9c5cf;
  --dim:#9b97a3;
  --green:#34c05a;
}
*{box-sizing:border-box;margin:0;padding:0}
html,body{width:1200px;height:4677px;overflow:hidden}
body{background:var(--bg);color:var(--text);font-family:'Inter',sans-serif;font-size:14px;line-height:1.55}
.wrap{width:960px;margin:0 auto;position:relative;height:100%}
h1,h2,h3{font-family:'Playfair Display',serif}
h2.section-title{font-size:31px;font-weight:700;text-align:center;letter-spacing:-.3px;position:absolute;left:0;right:0}
b{font-weight:700;color:#fff}
section,header,footer{position:relative}

.btn{display:inline-block;border-radius:24px;font-size:13px;font-weight:600;padding:11px 16px;color:#fff;text-decoration:none;white-space:nowrap}
.btn-primary{background:var(--pink-grad);box-shadow:0 6px 22px rgba(232,80,125,.45)}
.btn-ghost{border:1px solid #4a4652;background:transparent}

/* nav */
.nav{height:58px;background:#0d0b12;border-bottom:1px solid #1f1c26}
.nav .wrap{display:flex;align-items:center;justify-content:space-between}
.brand{display:flex;align-items:center;gap:8px;font-family:'Playfair Display',serif;font-weight:700;font-size:15px;color:#fff}
.brand-dot{width:12px;height:12px;border-radius:50%;background:var(--pink)}
.nav-links{display:flex;align-items:center;gap:26px;font-size:13px;font-weight:500}
.nav-links .btn{padding:8px 14px;font-size:12.5px}

/* hero */
.hero{height:527px;background:radial-gradient(ellipse at 75% 60%,#4a2466 0%,#2b1640 40%,#1a1026 75%),#1a1026}
.hero h1{position:absolute;left:0;top:120px;font-size:49px;line-height:1.02;font-weight:800;letter-spacing:-.8px;width:520px}
.hero-lead{position:absolute;left:0;top:242px;width:450px;font-size:14px;line-height:1.72;color:var(--muted)}
.hero .btn{position:absolute;left:0;top:364px}
.hero-photo{position:absolute;left:588px;top:78px;width:236px;height:372px;border-radius:10px;background:linear-gradient(180deg,#5a2e74 0%,#3a1d55 55%,#2a1540 100%)}

/* problems */
.problems{height:545px}
.problems h2{top:95px}
.cards3{position:absolute;left:0;top:154px;display:grid;grid-template-columns:repeat(3,307px);gap:19px}
.pcard{background:var(--card);border:1px solid var(--card-line);border-radius:10px;height:246px;text-align:center;padding:38px 28px 0}
.pcard .emo{font-size:34px;line-height:1}
.pcard h3{color:var(--pink-soft);font-size:19px;font-weight:700;margin:28px 0 10px;line-height:1.2}
.pcard p{font-size:12.5px;line-height:1.75;color:var(--muted)}
.kicker{position:absolute;left:0;right:0;top:444px;text-align:center;color:var(--pink-soft);font-weight:700;font-size:15px}

/* why */
.why{height:650px}
.why h2{font-size:31px;font-weight:700;line-height:1.05;position:absolute;left:0;top:80px;width:400px}
.why .intro{position:absolute;left:0;top:158px;width:460px;color:var(--muted);font-size:14.5px;line-height:1.75}
.checks{position:absolute;left:0;top:228px;list-style:none}
.checks li{display:flex;align-items:center;gap:10px;font-size:12.8px;color:var(--muted);height:37px}
.tick{flex:none;width:14px;height:14px;border-radius:3px;background:var(--green);display:flex;align-items:center;justify-content:center}
.quote-box{position:absolute;left:0;top:442px;width:454px;height:85px;background:#1c1a22;border:1px solid var(--card-line);border-left:3px solid var(--pink);border-radius:8px;padding:18px 20px;font-style:italic;font-size:12.8px;color:var(--pink-soft);line-height:1.6}
.why-photo{position:absolute;left:506px;top:166px;width:454px;height:301px;border-radius:12px;background:linear-gradient(120deg,#8a7a6c 0%,#c7b9a4 40%,#e8e4dc 62%,#6b5a50 100%);box-shadow:0 10px 40px rgba(90,40,120,.45)}

/* options */
.options{height:650px}
.options h2{top:70px}
.opt-grid{position:absolute;left:0;top:140px;display:grid;grid-template-columns:466px 466px;gap:28px}
.opt{background:var(--card);border:1px solid var(--card-line);border-radius:12px;height:449px;padding:32px 26px;position:relative}
.opt.featured{border:2px solid var(--pink);box-shadow:0 0 50px rgba(232,80,125,.22)}
.badge{position:absolute;top:-12px;left:50%;transform:translateX(-50%);background:var(--pink);font-size:11px;font-weight:600;padding:3px 12px;border-radius:12px}
.opt h3{font-size:20px;font-weight:700;display:flex;align-items:center;gap:12px}
.clock{width:26px;height:26px;border-radius:50%;background:#e9e6ef;display:inline-block}
.opt .pre{font-size:12.5px;color:var(--muted);margin-top:20px}
.opt ul{list-style:none;margin-top:22px}
.opt li{font-size:12.5px;color:var(--muted);height:33px;padding-left:20px;position:relative}
.opt li::before{content:"";position:absolute;left:2px;top:8px;width:5px;height:5px;border-radius:50%;background:var(--pink)}
.price{text-align:center;color:var(--pink-soft);font-size:27px;font-weight:700}
.vat{text-align:center;font-size:11.5px;color:var(--dim)}
.opt .btn{position:absolute;left:26px;bottom:30px;font-size:12.5px;padding:10px 16px}
.incl{position:absolute;left:0;right:0;top:612px;text-align:center;font-size:12.5px;font-style:italic;color:var(--muted)}

/* unique */
.unique{height:740px}
.unique h2{top:150px}
.u-grid{position:absolute;left:0;top:224px;display:grid;grid-template-columns:repeat(4,220px);gap:26.6px}
.ucard{background:var(--card);border:1px solid var(--card-line);border-radius:10px;height:198px;text-align:center;padding:30px 18px 0}
.ucard .emo{font-size:28px;line-height:1}
.ucard h3{font-size:15px;font-weight:700;margin:22px 0 4px;line-height:1.2}
.ucard p{font-size:12px;color:var(--muted);line-height:1.7}
.results{position:absolute;left:0;top:466px;width:960px;height:252px;background:#16141c;border:1px solid #221f29;border-radius:12px;padding:26px}
.results h3{font-size:20px;font-weight:700;margin-bottom:14px}
.results ul{list-style:none}
.results li{font-size:13px;color:var(--muted);height:33px;display:flex;align-items:center;gap:12px}
.results li::before{content:"";flex:none;width:8px;height:8px;border-radius:50%;background:var(--pink)}

/* steps */
.steps{height:560px}
.steps h2{top:145px}
.step-row{position:absolute;left:0;top:216px;display:grid;grid-template-columns:repeat(4,220px);gap:26.6px}
.step{text-align:center}
.step .num{width:46px;height:46px;border-radius:50%;background:var(--pink-grad);margin:0 auto;display:flex;align-items:center;justify-content:center;font-weight:700;font-size:17px;box-shadow:0 4px 18px rgba(232,80,125,.45)}
.step h3{font-size:14.5px;font-weight:700;margin-top:18px;line-height:1.2}
.step p{font-size:12px;color:var(--muted);line-height:1.6;margin-top:4px}
.steps .btn{position:absolute;left:50%;transform:translateX(-50%);top:386px;font-size:12.5px}

/* testimonials */
.testis{height:404px}
.testis h2{top:40px}
.t-grid{position:absolute;left:0;top:104px;display:grid;grid-template-columns:repeat(3,304px);gap:24px}
.tcard{background:var(--card);border:1px solid var(--card-line);border-radius:10px;height:216px;padding:28px}
.tcard q{display:block;font-style:italic;font-size:14.5px;line-height:1.6;color:#e9e6ee;quotes:"„" "“"}
.tcard .who{margin-top:18px;color:var(--pink-soft);font-weight:700;font-size:12.5px;line-height:1.55}

/* cta */
.cta{height:250px;background:linear-gradient(90deg,#221533 0%,#3a1e56 60%,#4a2568 100%);text-align:center;padding-top:50px}
.cta h2{font-size:31px;font-weight:700}
.cta p{color:var(--muted);font-size:14.5px;margin-top:10px}
.cta .btns{display:flex;justify-content:center;gap:14px;margin-top:26px}
.cta .btn{font-size:12.5px}

/* footer */
.footer{height:293px;background:#0e0c13}
.footer .cols{display:grid;grid-template-columns:330px 330px 300px;padding-top:38px}
.footer h4{color:var(--pink-soft);font-family:'Playfair Display',serif;font-size:15px;font-weight:700;margin-bottom:10px}
.footer p,.footer li{font-size:12px;color:var(--dim);line-height:2.3;list-style:none}
.footer .brand{font-size:14px;margin-bottom:26px}
.icon-sq{display:inline-block;width:10px;height:8px;background:#c8d4e8;margin-right:4px;vertical-align:middle}
.icon-ph{display:inline-block;width:6px;height:11px;border:1px solid #888;border-radius:2px;margin-right:6px;vertical-align:middle}
.icon-gl{display:inline-block;width:10px;height:10px;border-radius:50%;background:#5ab0e0;margin-right:4px;vertical-align:middle}
.foot-bottom{position:absolute;left:0;right:0;top:210px;text-align:center;border-top:1px solid #1c1a22;padding-top:18px}
.foot-bottom p{font-size:11.5px;color:var(--dim);line-height:2.3}
.foot-bottom .ps{font-style:italic;color:var(--pink-soft)}
</style>
</head>
<body>

<header class="nav">
  <div class="wrap">
    <div class="brand"><span class="brand-dot"></span>Sabine Hollert</div>
    <nav class="nav-links">
      <span>Coaching</span><span>Optionen</span><span>Testimonials</span>
      <a class="btn btn-primary">Vorgespräch buchen</a>
    </nav>
  </div>
</header>

<section class="hero">
  <div class="wrap">
    <h1>Stärken erkennen. Potenziale entfalten.</h1>
    <p class="hero-lead"><b>Pferdegestütztes Einzelcoaching</b> – der ehrlichste Spiegel für Ihre Führungswirkung.<br><b>Halb- oder Ganztag</b> für Führungskräfte, die <b>Substanz statt Standard</b> suchen.</p>
    <a class="btn btn-primary">Jetzt Vorgespräch buchen</a>
    <div class="hero-photo" role="img" aria-label="Porträt der Coachin vor violettem Hintergrund"></div>
  </div>
</section>

<section class="problems">
  <div class="wrap">
    <h2 class="section-title">Hier stehst du gerade?</h2>
    <div class="cards3">
      <div class="pcard"><div class="emo">😤</div><h3>Machtlos in Konflikten</h3><p>Trotz fachlicher Stärke fehlt dir die Durchsetzungskraft in schwierigen Situationen.</p></div>
      <div class="pcard"><div class="emo">😔</div><h3>Respekt fehlt</h3><p>Du wirst nicht ernst genommen und musst dir Aufmerksamkeit erkämpfen.</p></div>
      <div class="pcard"><div class="emo">😟</div><h3>Zweifel an Führungskompetenz</h3><p>Du bekommst nur Nettigkeiten statt ehrlichem, konstruktivem Feedback.</p></div>
    </div>
    <p class="kicker">Zeit für 500 kg Wahrheit.</p>
  </div>
</section>

<section class="why">
  <div class="wrap">
    <h2>Warum Pferdecoaching funktioniert</h2>
    <p class="intro">Ein Pferd kann nicht lügen – es reagiert auf deine echte Energie und gibt sofortiges, ungefiltertes Feedback.</p>
    <ul class="checks">
      <li><span class="tick"><svg width="10" height="10" viewBox="0 0 10 10"><path d="M2 5.2l2 2 4-4.4" stroke="#fff" stroke-width="1.6" fill="none"/></svg></span><span>Kann nicht lügen – reagiert auf <b>deine echte Energie</b></span></li>
      <li><span class="tick"><svg width="10" height="10" viewBox="0 0 10 10"><path d="M2 5.2l2 2 4-4.4" stroke="#fff" stroke-width="1.6" fill="none"/></svg></span><span>Ist nicht beeindruckt von <b>Titel oder Status</b></span></li>
      <li><span class="tick"><svg width="10" height="10" viewBox="0 0 10 10"><path d="M2 5.2l2 2 4-4.4" stroke="#fff" stroke-width="1.6" fill="none"/></svg></span><span>Gibt <b>sofortiges Feedback</b></span></li>
      <li><span class="tick"><svg width="10" height="10" viewBox="0 0 10 10"><path d="M2 5.2l2 2 4-4.4" stroke="#fff" stroke-width="1.6" fill="none"/></svg></span><span>Urteilt nicht – es <b>spiegelt</b></span></li>
      <li><span class="tick"><svg width="10" height="10" viewBox="0 0 10 10"><path d="M2 5.2l2 2 4-4.4" stroke="#fff" stroke-width="1.6" fill="none"/></svg></span><span>Reagiert auf das, was Menschen <b>spüren</b>, aber selten aussprechen</span></li>
    </ul>
    <div class="quote-box">„Das Pferd zeigt dir in 5 Minuten mehr als Jahre an Feedback-Gesprächen.“</div>
    <div class="why-photo" role="img" aria-label="Pferd im Seminarraum vor einem Flipchart, daneben die Coachin"></div>
  </div>
</section>

<section class="options">
  <div class="wrap">
    <h2 class="section-title">Deine Optionen</h2>
    <div class="opt-grid">
      <div class="opt">
        <h3><span class="clock"></span>Halbtags-Intensiv (4h)</h3>
        <ul style="margin-top:28px">
          <li>K.E.R.N.-Potentialanalyse</li>
          <li>Einführung &amp; erste Begegnung mit dem Pferd</li>
          <li>Grundlagen <b>Führungspräsenz</b></li>
          <li><b>Blinde Flecken</b> erkennen</li>
          <li><b>Videoanalyse</b> &amp; konkrete <b>Next Steps</b></li>
        </ul>
        <div class="price" style="margin-top:26px">1.250 €</div>
        <div class="vat">zzgl. MwSt.</div>
        <a class="btn btn-ghost">Halbtag buchen</a>
      </div>
      <div class="opt featured">
        <span class="badge">Empfohlen</span>
        <h3><span class="clock"></span>Ganztags-Intensiv (8h)</h3>
        <p class="pre">Alles aus <b>Halbtag</b>, plus:</p>
        <ul>
          <li>Tiefe Arbeit an <b>Führungsmustern</b></li>
          <li><b>Szenarien</b> &amp; schwierige Situationen durchspielen</li>
          <li>Ausführliche <b>Videoanalyse (Einzelszenen)</b></li>
          <li><b>60-Tage Entwicklungsplan</b></li>
        </ul>
        <div class="price" style="margin-top:38px">2.500 €</div>
        <div class="vat">zzgl. MwSt.</div>
        <a class="btn btn-primary">Ganztag buchen</a>
      </div>
    </div>
    <p class="incl"><b>Inklusive:</b> Halle, Seminarraum, Material, Verpflegung, Teilnahmebescheinigung</p>
  </div>
</section>

<section class="unique">
  <div class="wrap">
    <h2 class="section-title">Was macht dieses Coaching einzigartig?</h2>
    <div class="u-grid">
      <div class="ucard"><div class="emo">🎯</div><h3>Sofortiges, ungefiltertes Feedback</h3><p>Pure Wahrheit über deine Wirkung</p></div>
      <div class="ucard"><div class="emo">📹</div><h3>Videoanalyse</h3><p>Körpersprache sehen, verstehen, verbessern</p></div>
      <div class="ucard"><div class="emo">⚡</div><h3>Sofort umsetzbar</h3><p>Was du <b>morgen</b> anders machst</p></div>
      <div class="ucard"><div class="emo">🧠</div><h3>Tiefe Selbsterkenntnis</h3><p>Muster &amp; blinde Flecken erkennen</p></div>
    </div>
    <div class="results">
      <h3>Deine Ergebnisse nach einem Tag</h3>
      <ul>
        <li><span>Du weißt, <b>wie</b> du wirklich wirkst</span></li>
        <li><span>Worte &amp; Körpersprache <b>alignen</b></span></li>
        <li><span>Du steuerst Präsenz: <b>Autorität ohne Dominanz</b></span></li>
        <li><span>Vertrauen durch <b>Klarheit und Ruhe</b></span></li>
        <li><span><b>Authentische</b> Führung statt Rolle</span></li>
      </ul>
    </div>
  </div>
</section>

<section class="steps">
  <div class="wrap">
    <h2 class="section-title">So läuft's ab</h2>
    <div class="step-row">
      <div class="step"><div class="num">1</div><h3>Kostenloses Vorgespräch (30 Min.)</h3><p>Ziele klären &amp; Fit prüfen</p></div>
      <div class="step"><div class="num">2</div><h3>Termin &amp; Vorbereitung</h3><p>Anfahrt, Ablauf, was mitzubringen ist</p></div>
      <div class="step"><div class="num">3</div><h3>Dein Coaching-Tag</h3><p>4/8h intensiv mit Pferd, K.E.R.N., Videoanalyse, Next Steps</p></div>
      <div class="step"><div class="num">4</div><h3>Follow-up (optional)</h3><p>30 Tage später: Umsetzung &amp; weitere Schritte</p></div>
    </div>
    <a class="btn btn-ghost">Kostenloses Vorgespräch sichern</a>
  </div>
</section>

<section class="testis">
  <div class="wrap">
    <h2 class="section-title">Was Führungskräfte sagen</h2>
    <div class="t-grid">
      <div class="tcard"><q>In 10 Minuten mehr verstanden als in 20 Jahren Karriere. Brutal ehrlich – genau das, was ich brauchte.</q><div class="who">Tobias Lenhardt<br>Geschäftsführer</div></div>
      <div class="tcard"><q>Ich sah, wie meine Körpersprache meine Worte konterkarierte. Das war der Wendepunkt.</q><div class="who">Dr. Miriam Sauer<br>Abteilungsleiterin</div></div>
      <div class="tcard"><q>Die Videoanalyse war heftig – und heilsam. Seitdem folgt mein Team anders.</q><div class="who">Jonas Brettner<br>Teamleiter</div></div>
    </div>
  </div>
</section>

<section class="cta">
  <h2>Bereit für 500 kg Wahrheit?</h2>
  <p>Das Pferd lügt nicht. Bist du bereit für die Wahrheit über deine Führungswirkung?</p>
  <div class="btns">
    <a class="btn btn-primary">Ganztag buchen – 2.500 €</a>
    <a class="btn btn-ghost">Halbtag buchen – 1.250 €</a>
  </div>
</section>

<footer class="footer">
  <div class="wrap">
    <div class="cols">
      <div>
        <div class="brand"><span class="brand-dot"></span>Sabine Hollert</div>
        <p>Pferdegestütztes Leadership-Coaching</p>
      </div>
      <div>
        <h4>Kontakt</h4>
        <ul>
          <li><span class="icon-sq"></span>[E-Mail einsetzen]</li>
          <li><span class="icon-ph"></span>[Telefon einsetzen]</li>
          <li><span class="icon-gl"></span>[Website einsetzen]</li>
        </ul>
      </div>
      <div>
        <h4>Garantie</h4>
        <p>Ein glasklares Bild deiner Führungswirkung<br>30 Tage E-Mail-Support nach dem Coaching</p>
      </div>
    </div>
    <div class="foot-bottom">
      <p>© 2025 – Alle Rechte vorbehalten.</p>
      <p class="ps">P.S.: Das Pferd lügt nicht. Bist du bereit für die Wahrheit?</p>
    </div>
  </div>
</footer>

</body>
</html>
```